Home care agency

Current website QTRBLOOMS.com. Need to update and reformat to different pages. use my info from my current website

Target Market(s)

adult children

Industry/Entity Type

Home Health

Coding

Coded - Design and coding required

Number of Pages Required

4 page

Font styles to use
Sans Serif

Colors
3276b5
33a6d7
3277b5
85cae6
85acd3

```html
<!DOCTYPE html>
<html lang="en">
<head>
<meta charset="utf-8">
<title>Qtr Blooms Health &amp; Home Services</title>
<link href="https://fonts.googleapis.com/css2?family=Tinos:wght@400;700&family=Open+Sans:wght@400;600&display=swap" rel="stylesheet">
<style>
:root{
  --blue-deep:#3276b5;
  --blue:#33a6d7;
  --blue-mid:#3277b5;
  --sky:#85cae6;
  --steel:#85acd3;
  --ink:#333333;
  --ink-soft:#555555;
  --footer:#2b2b2b;
  --white:#ffffff;
  --placeholder:#e3e6e9;
}
*{margin:0;padding:0;box-sizing:border-box}
html,body{width:1200px;height:4098px;overflow:hidden;background:var(--white)}
body{position:relative;font-family:"Open Sans",Arial,sans-serif;color:var(--ink)}
.abs{position:absolute}
.serif{font-family:"Tinos","Times New Roman",serif}

/* header */
.top-stripe{left:0;top:0;width:1200px;height:9px;background:var(--blue)}
.call{left:82px;top:28px;font-size:13px;display:flex;align-items:center;gap:8px;color:var(--ink-soft)}
.call strong{color:var(--blue-deep);font-weight:600}
.employment{left:920px;top:8px;width:186px;height:33px;background:var(--blue-deep);color:#fff;font-family:"Tinos",serif;font-size:14px;display:flex;align-items:center;justify-content:center;clip-path:polygon(6% 0,100% 0,94% 100%,0 100%)}
.nav{left:0;top:72px;width:1200px;height:44px;background:var(--blue)}
.nav a{position:absolute;top:0;height:44px;line-height:44px;color:#fff;text-decoration:none;font-family:"Tinos",serif;font-size:14px;transform:translateX(-50%)}
.nav a.active{background:var(--blue-deep);width:89px;text-align:center;transform:none}
.brand{left:523px;top:23px;width:144px;height:144px;border-radius:50%;background:#fff;border:3px solid var(--sky);display:flex;align-items:center;justify-content:center;z-index:3}
.brand span{font-family:"Tinos",serif;font-size:20px;color:var(--blue-deep)}

/* hero */
.hero-photo{left:0;top:116px;width:1200px;height:680px;background:linear-gradient(120deg,#6e5a4a 0%,#a58d78 35%,#cdbba8 55%,#8d7564 80%,#5d4a3e 100%)}
.hero-text{left:0;width:1200px;text-align:center;color:#fff}
.hero-kicker{top:340px;font-size:34px}
.hero-title{top:375px;font-size:62px}
.hero-sub{top:444px;font-size:13px}
.hero-btn{left:479px;top:493px;width:239px;height:42px;border-radius:21px;background:var(--blue-deep);color:#fff;font-family:"Tinos",serif;font-size:14px;display:flex;align-items:center;justify-content:center}
.hero-wave{left:0;top:620px;width:1200px;height:190px}

/* about */
.h2{font-family:"Tinos",serif;font-size:36px;color:var(--ink);font-weight:400;letter-spacing:.5px}
.about-title{left:81px;top:925px}
.about-text{left:80px;top:1005px;width:460px;font-size:13px;line-height:28px;color:var(--ink-soft)}
.btn-pill{background:var(--blue);color:#fff;border-radius:22px;display:flex;align-items:center;justify-content:center;font-family:"Tinos",serif;font-size:14px}
.about-btn{left:81px;top:1198px;width:161px;height:45px}
.portrait-ring{left:625px;top:830px;width:456px;height:456px;border-radius:50%;border:14px solid #d9ecf6}
.portrait{left:654px;top:859px;width:398px;height:398px;border-radius:50%;background:radial-gradient(circle at 50% 45%,#c9b9ae 0%,#8c7d83 55%,#4e4558 100%)}
.name-pill{left:684px;top:1213px;width:354px;height:68px;border-radius:34px;background:var(--steel);color:#fff;font-family:"Tinos",serif;font-size:38px;display:flex;align-items:center;justify-content:center}

/* skilled services */
.skilled-title{left:0;top:1360px;width:1200px;text-align:center}
.service{top:1470px;width:200px;text-align:center;transform:translateX(-50%);font-family:"Tinos",serif;font-size:22px;line-height:29px;color:var(--ink)}
.service svg{display:block;margin:0 auto 14px}
.arrow{top:1528px}

/* non-medical */
.nm-panel{left:0;top:1735px;width:512px;height:395px;background:var(--sky)}
.nm-photo{left:520px;top:1735px;width:680px;height:395px;background:linear-gradient(110deg,#cfc6b6 0%,#e8ddd0 40%,#9fae7d 75%,#6f8a54 100%)}
.nm-title{left:83px;top:1775px;line-height:44px}
.nm-list{left:99px;top:1893px;list-style:none}
.nm-list li{height:34.7px;display:flex;align-items:center;gap:10px;font-size:13px;color:var(--ink-soft)}

/* benefits */
.benefits-title{left:0;top:2190px;width:1200px;text-align:center}
.benefit-arc{left:400px;top:2350px;width:420px;height:420px;border-radius:50%;border:18px solid #f1f5f9}
.b-circle{width:100px;height:100px;border-radius:50%;border:3px solid var(--blue-deep);background:#fff;display:flex;align-items:center;justify-content:center}
.b-text{font-size:13px;line-height:28px;color:var(--ink-soft)}
.ornament-slot{left:516px;top:2420px;width:180px;height:150px;background:var(--placeholder)}

/* why choose */
.why-photo{left:0;top:2639px;width:668px;height:395px;background:linear-gradient(120deg,#c9a98f 0%,#ecd6c4 40%,#d7e1ea 70%,#5e86b3 100%)}
.why-panel{left:676px;top:2639px;width:524px;height:395px;background:var(--sky)}
.why-title{left:748px;top:2695px}
.why-text{left:746px;width:380px;font-size:13px;line-height:28px;color:var(--ink-soft)}

/* schedule */
.sched-title{left:81px;top:3120px}
.sched-list{left:86px;top:3199px;width:490px;list-style:none}
.sched-list li{position:relative;padding-left:32px;font-size:13px;line-height:28px;color:var(--ink-soft);margin-bottom:28px}
.sched-list li::before{content:"";position:absolute;left:0;top:12px;width:5px;height:5px;border-radius:50%;background:var(--blue)}
.divider{left:81px;top:3442px;width:520px;height:1px;background:#dcdcdc}
.pay-title{left:81px;top:3478px}
.pay-text{left:81px;top:3545px;width:490px;font-size:13px;line-height:28px;color:var(--ink-soft)}
.map{left:676px;top:3034px;width:524px;height:587px;background:linear-gradient(135deg,#2f6db0 0%,#4f8cc8 45%,#dfe8f2 75%,#ffffff 100%)}

/* footer */
.footer-wave{left:0;top:3600px;width:1200px;height:498px}
.f-head{font-family:"Tinos",serif;font-size:18px;color:#fff}
.f-links{left:84px;top:3862px;list-style:none}
.f-links li{height:28px;display:flex;align-items:center;gap:10px;font-size:13px;color:#fff}
.f-links li::before{content:"";width:4px;height:4px;border-radius:50%;background:var(--blue)}
.f-line{font-size:13px;color:#fff;display:flex;align-items:center;gap:14px}
.socials{left:415px;top:3995px;display:flex;gap:10px}
.socials span{width:25px;height:25px;border-radius:50%;background:#fff}
.contact-box{left:759px;top:3689px;width:322px;height:395px;background:var(--blue-deep);border:3px solid #fff}
.contact-box h3{position:absolute;left:0;top:28px;width:100%;text-align:center;font-family:"Tinos",serif;font-weight:400;font-size:28px;line-height:32px;color:#fff}
.fld-label{left:31px;font-size:12px;line-height:14px;color:#fff}
.fld{left:31px;width:251px;height:28px;border-radius:14px;background:#fff}
.fld.msg{height:67px;border-radius:0}
.submit{left:27px;top:334px;width:257px;height:31px;border-radius:16px;background:var(--blue);color:#fff;font-family:"Tinos",serif;font-size:14px;display:flex;align-items:center;justify-content:center}
.copy{left:0;top:4074px;width:1200px;height:24px;background:var(--blue);color:#fff;font-size:12px;line-height:24px;padding-left:81px}
</style>
</head>
<body>

<!-- header -->
<div class="abs top-stripe"></div>
<div class="abs call">
  <svg width="22" height="22" viewBox="0 0 24 24"><path fill="#3276b5" d="M6.6 10.8a15 15 0 0 0 6.6 6.6l2.2-2.2a1 1 0 0 1 1-.25 11.4 11.4 0 0 0 3.6.57 1 1 0 0 1 1 1V20a1 1 0 0 1-1 1A17 17 0 0 1 3 4a1 1 0 0 1 1-1h3.5a1 1 0 0 1 1 1c0 1.25.2 2.45.57 3.57a1 1 0 0 1-.25 1z"/></svg>
  <span><strong>Call us Now</strong> 781-555-0142</span>
</div>
<div class="abs employment">Employment Application</div>
<nav class="abs nav">
  <a class="active" style="left:81px">Home</a>
  <a style="left:255px">About</a>
  <a style="left:405px">Services</a>
  <a style="left:796px">Why choose Home Care</a>
  <a style="left:950px">Career</a>
  <a style="left:1057px">Cotact</a>
</nav>
<div class="abs brand"><span>Qtr Blooms</span></div>

<!-- hero -->
<div class="abs hero-photo" role="img" aria-label="Photo of a smiling nurse caring for an elderly man at home"></div>
<div class="abs hero-text serif hero-kicker">Providing Care Throughout the South Shore</div>
<div class="abs hero-text serif hero-title">Health &amp; home Services</div>
<div class="abs hero-text hero-sub">Providing quality care services for over 18 years</div>
<div class="abs hero-btn">REQUEST AN APPOINMENT</div>
<svg class="abs hero-wave" viewBox="0 0 1200 190" preserveAspectRatio="none">
  <path fill="#33a6d7" d="M0 70 C180 10 360 90 560 120 C760 150 950 40 1200 20 L1200 190 L0 190Z"/>
  <path fill="#ffffff" d="M0 110 C200 60 380 130 580 150 C800 170 980 80 1200 70 L1200 190 L0 190Z"/>
</svg>

<!-- about -->
<h2 class="abs h2 about-title">ABOUT</h2>
<p class="abs about-text">Qtr Blooms Health Services is owned and operated by Marianne Costa. Marianne is a registered nurse and has been in the health care system since 2001. She has specialized in home care, cardiology, trauma and critical care. She invests in future caregivers and has taught for the nursing programs at Bayview University, Coastal Health Institute, and Mariner College.</p>
<div class="abs btn-pill about-btn">READ MORE</div>
<div class="abs portrait-ring"></div>
<div class="abs portrait" role="img" aria-label="Portrait photo of the agency owner, a registered nurse"></div>
<div class="abs name-pill">Marianne Costa</div>

<!-- skilled care services -->
<h2 class="abs h2 skilled-title">SKILLED CARE SERVICES</h2>
<svg class="abs arrow" style="left:24px" width="34" height="28" viewBox="0 0 34 28"><path d="M32 14H4M14 3 3 14l11 11" fill="none" stroke="#33a6d7" stroke-width="2.5"/></svg>
<svg class="abs arrow" style="left:1142px" width="34" height="28" viewBox="0 0 34 28"><path d="M2 14h28M20 3l11 11-11 11" fill="none" stroke="#3276b5" stroke-width="2.5"/></svg>

<div class="abs service" style="left:170px">
  <svg width="64" height="90" viewBox="0 0 64 90"><rect x="4" y="8" width="56" height="78" rx="4" fill="#85cae6" stroke="#3276b5" stroke-width="3"/><rect x="20" y="2" width="24" height="12" rx="3" fill="#3276b5"/><g stroke="#3276b5" stroke-width="3" fill="none"><path d="M12 32l4 4 6-7M28 33h22M12 50l4 4 6-7M28 51h22M12 68l4 4 6-7M28 69h22"/></g></svg>
  Nursing<br>Assessment</div>
<div class="abs service" style="left:380px">
  <svg width="76" height="90" viewBox="0 0 76 90"><rect x="4" y="8" width="56" height="76" rx="4" fill="#85cae6" stroke="#3276b5" stroke-width="3"/><rect x="20" y="2" width="24" height="12" rx="3" fill="#3276b5"/><path d="M32 22v18M23 31h18M14 52h36M14 62h28M14 72h22" stroke="#3276b5" stroke-width="3"/><circle cx="60" cy="72" r="13" fill="#fff" stroke="#3276b5" stroke-width="3"/><path d="M54 72l4 4 8-8" stroke="#3276b5" stroke-width="3" fill="none"/></svg>
  Medication<br>Management</div>
<div class="abs service" style="left:592px">
  <svg width="80" height="80" viewBox="0 0 80 80"><g transform="rotate(45 40 40)"><rect x="28" y="0" width="24" height="80" rx="6" fill="#85cae6" stroke="#3276b5" stroke-width="3"/><rect x="0" y="28" width="80" height="24" rx="6" fill="#85cae6" stroke="#3276b5" stroke-width="3"/><rect x="30" y="30" width="20" height="20" fill="#3276b5"/></g></svg>
  Wound Care</div>
<div class="abs service" style="left:802px">
  <svg width="92" height="76" viewBox="0 0 92 76"><path d="M36 4h20v16h16v20H56v16H36V40H20V20h16z" fill="#3276b5"/><path d="M4 30l10 30 22 12M88 30L78 60 56 72" fill="none" stroke="#3276b5" stroke-width="3"/><path d="M12 44l14 16M80 44L66 60" stroke="#85cae6" stroke-width="6" stroke-linecap="round"/></svg>
  Care Plan<br>Management</div>
<div class="abs service" style="left:1012px">
  <svg width="64" height="80" viewBox="0 0 64 80"><rect x="18" y="2" width="28" height="14" rx="3" fill="#fff" stroke="#3276b5" stroke-width="3"/><path d="M32 5v8M28 9h8" stroke="#3276b5" stroke-width="2"/><circle cx="32" cy="32" r="14" fill="#85cae6" stroke="#3276b5" stroke-width="3"/><path d="M4 78c0-18 12-28 28-28s28 10 28 28z" fill="#85cae6" stroke="#3276b5" stroke-width="3"/></svg>
  Medical Care<br>Assistance</div>

<!-- non-medical -->
<div class="abs nm-panel"></div>
<div class="abs nm-photo" role="img" aria-label="Photo of a caregiver reading a book with an elderly woman holding a cup"></div>
<h2 class="abs h2 nm-title">NON-MEDICAL<br>SERVICES</h2>
<ul class="abs nm-list">
  <li><svg width="18" height="16" viewBox="0 0 18 16"><path d="M1 8l5 6L17 1" fill="none" stroke="#3276b5" stroke-width="3"/></svg>Live-In Care</li>
  <li><svg width="18" height="16" viewBox="0 0 18 16"><path d="M1 8l5 6L17 1" fill="none" stroke="#3276b5" stroke-width="3"/></svg>Respite Care</li>
  <li><svg width="18" height="16" viewBox="0 0 18 16"><path d="M1 8l5 6L17 1" fill="none" stroke="#3276b5" stroke-width="3"/></svg>Assisting with Daily Living Activities</li>
  <li><svg width="18" height="16" viewBox="0 0 18 16"><path d="M1 8l5 6L17 1" fill="none" stroke="#3276b5" stroke-width="3"/></svg>Meal Preparations</li>
  <li><svg width="18" height="16" viewBox="0 0 18 16"><path d="M1 8l5 6L17 1" fill="none" stroke="#3276b5" stroke-width="3"/></svg>Companionship</li>
  <li><svg width="18" height="16" viewBox="0 0 18 16"><path d="M1 8l5 6L17 1" fill="none" stroke="#3276b5" stroke-width="3"/></svg>Homemaking</li>
</ul>

<!-- client benefits -->
<h2 class="abs h2 benefits-title">CLIENT BENEFITS</h2>
<div class="abs benefit-arc"></div>
<div class="abs ornament-slot" role="img" aria-label="Space for a decorative seashell illustration"></div>

<div class="abs b-circle" style="left:427px;top:2290px">
  <svg width="46" height="46" viewBox="0 0 46 46"><path d="M18 4h10v8h8v10h-8v8H18v-8h-8V12h8z" fill="none" stroke="#33a6d7" stroke-width="2.5"/><path d="M4 34h12l8 4 16-6" fill="none" stroke="#3276b5" stroke-width="2.5"/></svg></div>
<div class="abs b-circle" style="left:663px;top:2290px">
  <svg width="46" height="40" viewBox="0 0 46 40"><rect x="3" y="4" width="30" height="20" rx="3" fill="none" stroke="#3276b5" stroke-width="2.5"/><rect x="13" y="12" width="30" height="20" rx="3" fill="#85cae6" stroke="#3276b5" stroke-width="2.5"/></svg></div>
<div class="abs b-circle" style="left:332px;top:2441px">
  <svg width="46" height="36" viewBox="0 0 46 36"><rect x="3" y="4" width="40" height="28" rx="3" fill="none" stroke="#3276b5" stroke-width="2.5"/><path d="M3 6l20 15L43 6" fill="none" stroke="#33a6d7" stroke-width="2.5"/></svg></div>
<div class="abs b-circle" style="left:758px;top:2441px">
  <svg width="44" height="44" viewBox="0 0 44 44"><circle cx="22" cy="22" r="14" fill="none" stroke="#3276b5" stroke-width="4" stroke-dasharray="5 3"/><circle cx="22" cy="22" r="8" fill="none" stroke="#33a6d7" stroke-width="2.5"/><text x="22" y="27" font-size="12" text-anchor="middle" fill="#3276b5" font-family="Open Sans,sans-serif">$</text></svg></div>

<p class="abs b-text" style="left:120px;top:2311px;width:272px;text-align:right">Continuity of care with same caregiver for each client on a regular basis.</p>
<p class="abs b-text" style="left:808px;top:2311px;width:300px">Ongoing communications to client's family by phone or email on a weekly basis (if desired.)</p>
<p class="abs b-text" style="left:60px;top:2463px;width:252px;text-align:right">Open communication with owner by phone or email.</p>
<p class="abs b-text" style="left:885px;top:2463px;width:260px">Streamlined payment process.</p>

<!-- why choose us -->
<div class="abs why-photo" role="img" aria-label="Photo of a smiling nurse embracing an elderly woman"></div>
<div class="abs why-panel"></div>
<h2 class="abs h2 why-title">WHY CHOOSE US</h2>
<p class="abs why-text" style="top:2778px">Home care is a cost-effective option that allows clients the ability to receive one-on-one care in the comfort of their own home.</p>
<p class="abs why-text" style="top:2889px">Home care also provides peace of mind to a client's family, near or far, without taking away a client's independence or privacy.</p>

<!-- schedule & payment -->
<h2 class="abs h2 sched-title">CARE SCHEDULE/FREQUENCY</h2>
<ul class="abs sched-list">
  <li>Qtr Blooms non-medical visits require a four hour minimum visit.</li>
  <li>There are no weekly minimum for medical or non-medical visits.</li>
  <li>Clients needing 24-hour care can save up 30% off of services by using a live-in caregiver. (Live-in caregiver requires personal bedroom and bathroom.)</li>
</ul>
<div class="abs divider"></div>
<h2 class="abs h2 pay-title">PAYMENT OPTIONS</h2>
<p class="abs pay-text">Qtr Blooms currently accepts check for service payments (with plans for online payments late 2018.)</p>
<div class="abs map" role="img" aria-label="Map of South Shore towns with the service area shaded blue"></div>

<!-- footer -->
<svg class="abs footer-wave" viewBox="0 0 1200 498" preserveAspectRatio="none">
  <path fill="#33a6d7" d="M0 60 C240 0 520 90 760 40 C920 10 1080 20 1200 50 L1200 498 L0 498Z"/>
  <path fill="#2b2b2b" d="M0 110 C260 50 540 140 780 95 C940 65 1090 70 1200 100 L1200 498 L0 498Z"/>
</svg>

<div class="abs f-head" style="left:83px;top:3826px">QUICK LINKS</div>
<ul class="abs f-links">
  <li>Home</li><li>About</li><li>Services</li><li>Why choose home care</li><li>Career</li><li>Contact</li>
</ul>

<div class="abs f-head" style="left:376px;top:3826px">CONTACT BY PHONE</div>
<div class="abs f-line" style="left:376px;top:3864px">
  <svg width="16" height="16" viewBox="0 0 24 24"><path fill="#33a6d7" d="M6.6 10.8a15 15 0 0 0 6.6 6.6l2.2-2.2a1 1 0 0 1 1-.25 11.4 11.4 0 0 0 3.6.57 1 1 0 0 1 1 1V20a1 1 0 0 1-1 1A17 17 0 0 1 3 4a1 1 0 0 1 1-1h3.5a1 1 0 0 1 1 1c0 1.25.2 2.45.57 3.57a1 1 0 0 1-.25 1z"/></svg>
  <span>Monday-Friday 9:00am-5:00pm at</span></div>
<div class="abs f-line" style="left:415px;top:3892px">781-555-0142</div>
<div class="abs f-head" style="left:376px;top:3921px">MAILING ADDRESS</div>
<div class="abs f-line" style="left:382px;top:3956px">
  <svg width="12" height="16" viewBox="0 0 12 16"><path fill="#33a6d7" d="M6 0a6 6 0 0 0-6 6c0 4.5 6 10 6 10s6-5.5 6-10a6 6 0 0 0-6-6zm0 8.5A2.5 2.5 0 1 1 6 3.5a2.5 2.5 0 0 1 0 5z"/></svg>
  <span>PO Box 48 Seaview, MA 02099</span></div>
<div class="abs socials" aria-label="Social media links"><span></span><span></span><span></span><span></span><span></span></div>

<div class="abs contact-box">
  <h3>CONTACT US</h3>
  <div class="abs fld-label" style="top:68px">Full Name</div>
  <div class="abs fld" style="top:85px"></div>
  <div class="abs fld-label" style="top:119px">Phone#</div>
  <div class="abs fld" style="top:136px"></div>
  <div class="abs fld-label" style="top:170px">Email Address</div>
  <div class="abs fld" style="top:187px"></div>
  <div class="abs fld-label" style="top:222px">Message</div>
  <div class="abs fld msg" style="top:240px"></div>
  <div class="abs submit">SUBMIT NOW</div>
</div>

<div class="abs copy">Copyright © 2019 Qtr Blooms. All Right Reserved</div>

</body>
</html>
```